business card deign

Logo needs the following on it.
1. attached logo
2. Tagline - "From the first pour to the last song...we bring it all!"
3. Name- Delia Fenwick, Founder and CPO
4. Address - 418 E. Harlow Avenue, Ste 2204, Tampa, FL. 33719
5. Phone - 720.555.0187

```html
<!DOCTYPE html>
<html lang="en">
<head>
<meta charset="utf-8">
<title>Kelvara Business Card</title>
<link href="https://fonts.googleapis.com/css2?family=Montserrat:wght@400;700&display=swap" rel="stylesheet">
<style>
  :root {
    --stage: #e9e6e1;
    --card-dark: #1e1e1e;
    --ink: #111111;
    --paper: #ffffff;
    --band: #050505;
    --muted: #3a3a3a;
  }
  * { box-sizing: border-box; margin: 0; padding: 0; }
  html, body { width: 1200px; height: 931px; overflow: hidden; }
  body {
    background: var(--stage);
    font-family: "Montserrat", sans-serif;
    color: var(--ink);
    position: relative;
  }
  .card {
    position: absolute;
    width: 660px;
    height: 377px;
    border-radius: 22px;
    overflow: hidden;
    box-shadow: 0 14px 30px rgba(0,0,0,0.25);
  }
  .card-back {
    left: 40px;
    top: 40px;
    background: linear-gradient(120deg, var(--card-dark) 0%, var(--card-dark) 55%, #3c3c3c 100%);
  }
  .card-back .pattern-area {
    position: absolute;
    inset: 0;
    background: radial-gradient(circle at 62% 46%, #4a4a4a 0%, rgba(0,0,0,0) 45%);
  }
  .card-back .brand-mark {
    position: absolute;
    left: 370px;
    top: 150px;
    width: 60px;
    height: 60px;
    border-radius: 50%;
    background: var(--paper);
  }
  .card-front {
    left: 500px;
    top: 470px;
    background: var(--paper);
  }
  .brand {
    position: absolute;
    right: 40px;
    top: 70px;
    display: flex;
    align-items: center;
    gap: 14px;
  }
  .brand-dot {
    width: 34px; height: 34px; border-radius: 50%; background: var(--ink);
  }
  .brand-name {
    font-weight: 700;
    font-size: 34px;
    letter-spacing: 10px;
    color: var(--ink);
  }
  .rule-top {
    position: absolute;
    left: 220px; right: 30px; top: 132px;
    height: 1.5px; background: var(--ink);
  }
  .person { position: absolute; left: 40px; top: 166px; }
  .person-name { font-weight: 700; font-size: 30px; line-height: 1.1; }
  .person-title { font-size: 17px; color: var(--muted); margin-top: 4px; }
  .rule-mid {
    position: absolute; left: 40px; width: 250px; top: 234px;
    height: 1.5px; background: var(--ink);
  }
  .contacts { position: absolute; left: 40px; top: 244px; list-style: none; }
  .contacts li {
    display: flex; align-items: center; gap: 12px;
    font-size: 16px; height: 24px;
  }
  .contacts svg { width: 16px; height: 16px; flex: none; }
  .address {
    position: absolute; right: 36px; top: 170px;
    text-align: right; font-size: 16px; line-height: 1.35;
  }
  .band-line {
    position: absolute; left: 0; right: 0; bottom: 46px;
    height: 2px; background: var(--band);
  }
  .tagline-band {
    position: absolute; left: 0; right: 0; bottom: 0; height: 40px;
    background: var(--band); color: var(--paper);
    display: flex; align-items: center; justify-content: flex-end;
    padding-right: 40px; font-size: 15px;
  }
</style>
</head>
<body>
  <section class="card card-back">
    <div class="pattern-area" role="img" aria-label="Repeating brand mark pattern in glossy black tones"></div>
    <div class="brand-mark"></div>
  </section>

  <section class="card card-front">
    <div class="brand">
      <span class="brand-dot"></span>
      <span class="brand-name">KELVARA</span>
    </div>
    <div class="rule-top"></div>

    <div class="person">
      <h1 class="person-name">Delia Fenwick</h1>
      <p class="person-title">Founder and CPO</p>
    </div>
    <div class="rule-mid"></div>

    <ul class="contacts">
      <li>
        <svg viewBox="0 0 16 16"><path d="M3 1.5l2.5 0 1 3.5-1.6 1.2a8 8 0 0 0 4.9 4.9L11 9.5l3.5 1v2.5a1.5 1.5 0 0 1-1.5 1.5A12 12 0 0 1 1.5 3 1.5 1.5 0 0 1 3 1.5z" fill="#111"/></svg>
        720.555.0187
      </li>
      <li>
        <svg viewBox="0 0 16 16"><rect x="1" y="3" width="14" height="10" fill="#111"/><path d="M1 3l7 6 7-6" stroke="#fff" stroke-width="1.2" fill="none"/></svg>
        info@email.com
      </li>
      <li>
        <svg viewBox="0 0 16 16" fill="none" stroke="#111" stroke-width="1.4"><circle cx="8" cy="8" r="6.5"/><ellipse cx="8" cy="8" rx="3" ry="6.5"/><path d="M1.5 8h13M2.5 5h11M2.5 11h11"/></svg>
        www.websitename.com
      </li>
    </ul>

    <p class="address">418 E. Harlow Avenue, Ste 2204,<br>Tampa, FL. 33719</p>

    <div class="band-line"></div>
    <div class="tagline-band">From the first pour to the last song...we bring it all!</div>
  </section>
</body>
</html>
```